Velora Crest Label

Design a label for the new brand Velora Crest. The specific product label : Velora Crest Deep Moisturizing Conditioner.

You only need to design the front label.I have included the logo and a bottle jpeg. Please try your best.

Industry/Entity Type

Product

Requirements
Must have
• text you can use:
• For Dry, Damaged Hair
• Strengthening & Moisturizing Conditioner
• Moisture Infused
• Deep Penetrating Formula
• Used by Professionals
• 8.5oz/250ml

```html
<!DOCTYPE html>
<html lang="en">
<head>
<meta charset="utf-8">
<title>Velora Crest Deep Moisturizing Conditioner – Front Label</title>
<link rel="stylesheet" href="https://fonts.googleapis.com/css2?family=Oswald:wght@500;600&family=Source+Sans+3:wght@400&display=swap">
<style>
  :root {
    --canvas: #ffffff;
    --label-light: #fff4a6;
    --label-mid: #ffd92e;
    --label-deep: #f9b400;
    --band-yellow: #ffe600;
    --ink: #111111;
    --brand-ink: #3a2a05;
    --white: #ffffff;
    --hair-dark: #1e120b;
    --hair-mid: #4a2c1c;
    --hair-light: #7a5038;
    --note-ink: #231f20;
  }
  html, body {
    margin: 0;
    padding: 0;
    width: 1200px;
    height: 1200px;
    overflow: hidden;
    background: var(--canvas);
  }
  .artboard {
    position: relative;
    width: 1200px;
    height: 1200px;
  }
  .label {
    position: absolute;
    left: 198px;
    top: 402px;
    width: 234px;
    height: 660px;
    border-radius: 12px;
    overflow: hidden;
    background: linear-gradient(90deg, var(--label-light) 0%, var(--label-mid) 45%, var(--label-deep) 100%);
    font-family: "Oswald", "Arial Narrow", sans-serif;
  }
  .new-flag {
    position: absolute;
    left: 0;
    top: 0;
    width: 112px;
    height: 76px;
  }
  .brand-name {
    position: absolute;
    left: 0;
    right: 0;
    top: 540px;
    top: 548px;
  }
  .brand {
    position: absolute;
    top: 152px;
    left: 0;
    width: 100%;
    text-align: center;
    font-weight: 600;
    font-size: 34px;
    line-height: 1;
    letter-spacing: 0.5px;
    color: var(--brand-ink);
  }
  .product-band {
    position: absolute;
    left: 0;
    top: 304px;
    width: 100%;
    height: 28px;
    background: var(--band-yellow);
    text-align: center;
    font-weight: 600;
    font-size: 23px;
    line-height: 28px;
    color: var(--ink);
    letter-spacing: 0.2px;
  }
  .hero-photo {
    position: absolute;
    left: 0;
    top: 332px;
    width: 100%;
    height: 152px;
    background:
      radial-gradient(ellipse at 78% 55%, var(--hair-light) 0%, var(--hair-mid) 35%, transparent 70%),
      linear-gradient(100deg, var(--hair-dark) 0%, var(--hair-mid) 40%, var(--hair-dark) 100%);
  }
  .product-type {
    position: absolute;
    right: 10px;
    top: 338px;
    font-weight: 500;
    font-size: 13px;
    color: var(--white);
    letter-spacing: 0.3px;
  }
  .foil-stripe {
    position: absolute;
    left: 0;
    top: 484px;
    width: 100%;
    height: 12px;
    background: var(--band-yellow);
  }
  .benefits {
    position: absolute;
    left: 0;
    top: 536px;
    width: 100%;
    text-align: center;
    font-weight: 500;
    font-size: 13px;
    line-height: 21px;
    color: var(--ink);
    letter-spacing: 0.3px;
  }
  .volume {
    position: absolute;
    left: 0;
    top: 618px;
    width: 100%;
    text-align: center;
    font-weight: 500;
    font-size: 9px;
    color: var(--ink);
  }
  .callouts {
    position: absolute;
    left: 0;
    top: 0;
    width: 1200px;
    height: 1200px;
    pointer-events: none;
  }
  .callout-text {
    position: absolute;
    left: 66px;
    top: 784px;
    width: 70px;
    text-align: center;
    font-family: "Source Sans 3", "Myriad Pro", sans-serif;
    font-size: 19px;
    line-height: 23px;
    color: var(--note-ink);
  }
  .swatch-legend {
    position: absolute;
    left: 142px;
    top: 1104px;
    display: flex;
    align-items: center;
    gap: 18px;
    font-family: "Source Sans 3", "Myriad Pro", sans-serif;
    font-size: 21px;
    color: var(--note-ink);
  }
  .swatch {
    width: 17px;
    height: 17px;
    background: var(--band-yellow);
  }
</style>
</head>
<body>
<main class="artboard">
  <section class="label" aria-label="Velora Crest Deep Moisturizing Conditioner front label">
    <svg class="new-flag" viewBox="0 0 112 76" aria-hidden="false" role="img" aria-label="New">
      <polygon points="0,0 112,0 0,76" fill="#111111"/>
      <text x="24" y="38" transform="rotate(-22 38 32)" fill="#ffffff" font-family="Oswald, sans-serif" font-weight="600" font-size="18">NEW</text>
    </svg>
    <div class="brand">Velora Crest</div>
    <div class="product-band">DEEP MOISTURIZING</div>
    <div class="hero-photo" role="img" aria-label="Photo of a woman with long, glossy dark brown hair"></div>
    <div class="product-type">CONDITIONER</div>
    <div class="foil-stripe"></div>
    <p class="benefits" style="margin:0">DEEP MOISTURIZING<br>SOFTNESS AND SHINE</p>
    <div class="volume">8.5oz/250ml</div>
  </section>

  <svg class="callouts" viewBox="0 0 1200 1200" aria-hidden="true">
    <defs>
      <marker id="arrowhead" viewBox="0 0 10 10" refX="9" refY="5" markerWidth="7" markerHeight="7" orient="auto">
        <path d="M0,0 L10,5 L0,10 z" fill="#231f20"/>
      </marker>
    </defs>
    <line x1="132" y1="804" x2="204" y2="722" stroke="#231f20" stroke-width="1" marker-end="url(#arrowhead)"/>
    <line x1="134" y1="818" x2="258" y2="892" stroke="#231f20" stroke-width="1" marker-end="url(#arrowhead)"/>
  </svg>
  <div class="callout-text">Foiling<br>Area</div>

  <div class="swatch-legend"><span class="swatch"></span><span>Pantone 209 C &amp; Foiling Area</span></div>
</main>
</body>
</html>
```